Drug Sample Pack Design
Nausea Prevention Drug Packaging
Project: Drug Sample Pack Design
Creative Brief
I need a sample pack design for a new dietary supplement I am producing. I say sample pack, but it's not really a sample, that's how we are going to sell the drug, but it is packaged in the typical foil sample packs you see in stores. This is what I mean: (My favorite, but all four are good) http://www.pelvorasupply.example/images/Ventrolin-BX.gif http://fl2.trovimart.example/files/images/10161/single-dose-corvane-febrilex-10-packs~10160384.jpg http://beta.zembuy.example/img/item/117/499/357/o_mfZsnBHbgIjyxiw.jpg http://www.savingowl.example/blog/wp-content/uploads/2010/10/Fizzora_Tablet_Box.gif My product is called "Gastrelle" and the tagline is "Nausea Prevention for Alcohol Use" Your job is to sell me my product. It is marketed as a dietary supplement, not a drug so any claim you make must be supported by scientific evidence. Ours is, we are Doctor/Physician Approved and have done several Double Blind Clinical Trials "Clinically Approved". Our main competitors are products like Rumbo Max, http://www.rumbomax.example/ and Belvix, Pelks, other antacids. Our product shares the same active ingredient as all of those above, but we are marketing our product differently, for Nausea Prevention, not "Hangover Prevention" or as an "antacid" even though it is the same thing, it must not appear that way. Rumbo looks like something you would buy at a truck stop. It's trashy. Belvix make your kids want to eat them, they are fun, colorful etc... We want to be professional. The ventrolin bx pack I showed above really captures that. We want people to see "Gastrelle" and think, wow, this might actually work. This is professional, I trust this product. It is doctor approved, is has gone through a clinical trial, this looks not only safe, but effective. We think a good way to do that would be to have a diagram on the package depicting how our product works. We suspect the active ingredient of gastrelle, carbonate ion, forms a "protective lining" around the stomach. Normally, alcohol irritates this lining and causes it to produce lots of acid. When acid accumulates in the stomach, you get nauseous and vomit to get rid of the excess acid. Our active ingredient both prevents this irritation and neutralizes the acid, preventing nausea. So maybe have a diagram like this, but obviously this is way to ugly, draw it yourself or find something better, that includes some cartoon of Gastrelle protecting the stomach and/or neurtralizing acid and maybe if you can think of a way, to show that now, since acid is low, the brain is not signaled to throw up/vomit. http://images.lornapedia.example/2342474_com_500pxstoma.png Everything I've said is a suggestion, the winner will be the product that I want to buy the most. Sell me "Gastrelle" The winner will get first offer for all future graphic design for Dietary Supplements from Quillon Industries.
Health
College Students
Suggestions: This product must look professional. See the ventrolin bx image. This must include some sort of Doctor/Physician Approved or Clinically Proven message. Must also include "Nausea Prevention for Alcohol Use" Must include "Dietary Supplement" Include a link to my website, http://gastrelle.example (it isn't up yet) This is a dietary supplement and as such must include the standard ingredients label on the back. The active ingredient is 1000mg Calcium Carbonate per tablet. There are two tablets per package. Two tablets per serving. The diagram is optional, I think it might look good, but it's up to you. While I technically call these requirements, despite whatever I said, the winner will be the package that I want to buy the most. It's as simple as that. If you decide you want to change the name of my product, change my tagline, not do a diagram, completely go against all of my suggestions, but it still sells me the product, that is fine by me. Sell me "Gastrelle"

```html
<!DOCTYPE html>
<html lang="en">
<head>
<meta charset="utf-8">
<title>Gastrelle sample pack series</title>
<link rel="stylesheet" href="https://fonts.googleapis.com/css2?family=Open+Sans:ital,wght@0,400;0,600;0,700;0,800;1,700&display=swap">
<style>
  :root {
    --bg: #c9c9c9;
    --bg-stripe: #bdbdbd;
    --silver-hi: #f4f4f4;
    --silver-mid: #d6d6d6;
    --silver-lo: #a9a9a9;
    --ink: #4b4b4b;
    --ink-soft: #7a7a7a;
    --red: #d7361e;
    --green: #5a9f2b;
    --orange: #f09a12;
    --white: #ffffff;
    --note: #1f57a8;
  }
  * { box-sizing: border-box; margin: 0; padding: 0; }
  html, body { width: 1200px; height: 756px; overflow: hidden; }
  body {
    font-family: "Open Sans", Arial, sans-serif;
    background: repeating-linear-gradient(135deg, var(--bg) 0 6px, var(--bg-stripe) 6px 8px);
    position: relative;
  }
  .red { --accent: var(--red); }
  .green { --accent: var(--green); }
  .orange { --accent: var(--orange); }

  /* packet drawn at 280 x 340, then scaled into place */
  .packet {
    position: absolute;
    width: 280px;
    height: 340px;
    transform-origin: 0 0;
    transform: scale(.6);
    border-radius: 3px;
    overflow: hidden;
    background: linear-gradient(160deg, var(--silver-hi) 0%, var(--silver-mid) 45%, var(--silver-lo) 100%);
    box-shadow: 0 2px 6px rgba(0,0,0,.25);
  }
  .packet::before, .packet::after {
    content: ""; position: absolute; left: 0; right: 0; height: 6px;
    background: repeating-linear-gradient(90deg, rgba(0,0,0,.12) 0 2px, transparent 2px 4px);
    z-index: 3;
  }
  .packet::before { top: 0; }
  .packet::after { bottom: 0; }

  .band {
    position: absolute; top: 12px; left: 0; width: 190px; height: 28px;
    background: var(--accent);
    color: var(--white); font-weight: 700; font-style: italic; font-size: 15px;
    line-height: 28px; padding-left: 14px;
    clip-path: polygon(0 0, 100% 0, 92% 100%, 0 100%);
  }
  .badge {
    position: absolute; top: 8px; right: 12px; width: 64px; height: 64px; border-radius: 50%;
    background: radial-gradient(circle at 40% 40%, #ffffff 0%, #dfe6ee 55%, #9fb1c4 100%);
    border: 2px solid #ffffff;
  }
  .supplement {
    position: absolute; top: 52px; left: 16px;
    font-size: 14px; font-weight: 700; line-height: 1; color: var(--ink-soft);
  }
  .name {
    position: absolute; top: 74px; left: 14px;
    font-size: 44px; font-weight: 800; color: var(--ink); letter-spacing: -1px; line-height: 1.1;
  }
  .claims {
    position: absolute; top: 130px; left: 60px; width: 160px;
    text-align: center; font-size: 10px; font-weight: 700; color: var(--ink-soft); line-height: 1.3;
  }
  .claims .benefit { color: var(--accent); font-size: 11px; }
  .stomach {
    position: absolute; top: 190px; left: 110px; width: 140px; height: 110px;
    border-radius: 55% 45% 50% 60%;
    background: radial-gradient(circle at 45% 40%, #f3c35a 0%, #e2a63b 45%, #7bab3a 80%, #4e8a2a 100%);
    opacity: .9;
  }
  .swoosh { position: absolute; left: 0; bottom: 0; width: 280px; height: 80px; z-index: 1; }
  .dose {
    position: absolute; left: 16px; bottom: 14px; z-index: 2;
    color: var(--white); font-size: 12px; font-weight: 700; line-height: 1.2;
  }
  .dose small { display: block; font-weight: 400; font-size: 9px; }

  .packet.back { background: linear-gradient(160deg, #fbfbfb 0%, #e6e6e6 60%, #cfcfcf 100%); }
  .back .name { top: 18px; left: auto; right: 18px; font-size: 36px; }
  .icon-cut { position: absolute; top: 28px; left: 18px; width: 22px; height: 14px; }
  .facts {
    position: absolute; top: 80px; left: 18px; width: 170px;
    font-size: 8px; line-height: 1.35; color: var(--ink);
  }
  .facts h3 { font-size: 8.5px; font-weight: 700; margin-top: 8px; }
  .back .stomach { top: auto; left: auto; right: 20px; bottom: 90px; width: 100px; height: 84px; }
  .site {
    position: absolute; bottom: 16px; left: 0; right: 0; z-index: 2;
    text-align: center; color: var(--white); font-weight: 800; font-size: 20px;
  }

  .series-name {
    position: absolute; top: 62px; left: 856px;
    font-size: 56px; font-weight: 800; color: var(--white); letter-spacing: -1px; line-height: 1;
  }
  .series-note {
    position: absolute; top: 174px; left: 878px;
    font-size: 13px; font-weight: 700; font-style: italic; color: var(--note); line-height: 1.3;
  }

  .hang-card {
    position: absolute; left: 828px; top: 276px; width: 312px; height: 432px;
    border-radius: 14px;
    background: linear-gradient(170deg, var(--silver-hi), var(--silver-mid) 60%, var(--silver-lo));
    box-shadow: 0 3px 10px rgba(0,0,0,.3);
  }
  .hang-hole {
    position: absolute; top: 12px; left: 50%; width: 56px; height: 13px; margin-left: -28px;
    border-radius: 7px; background: var(--bg);
  }
  .card-supplement {
    position: absolute; top: 42px; left: 20px; width: 90px;
    font-size: 12px; font-weight: 700; color: var(--ink-soft); line-height: 1.15;
  }
  .card-name {
    position: absolute; top: 34px; right: 20px;
    font-size: 32px; font-weight: 800; color: var(--ink); letter-spacing: -1px; line-height: 1.1;
  }
  .hang-card .packet { left: 48px; top: 96px; transform: scale(.77); }
</style>
</head>
<body>

<!-- top row: fronts -->
<section class="packet front red" style="left:72px; top:113px;">
  <div class="band">Clinically Approved</div>
  <div class="badge" role="img" aria-label="Round emblem of tablets"></div>
  <p class="supplement">Dietary Supplement</p>
  <h2 class="name">gastrelle</h2>
  <p class="claims">Nausea Prevention<br>for Alcohol Use<br><span class="benefit">Protects Stomach<br>Neutralizes Acid</span></p>
  <div class="stomach" role="img" aria-label="Stomach illustration"></div>
  <svg class="swoosh" viewBox="0 0 280 80" preserveAspectRatio="none"><path d="M0 30 C90 70 190 10 280 20 L280 80 L0 80 Z" fill="var(--accent)"/></svg>
  <p class="dose">2 tablets · 1000 mg<small>Calcium Carbonate per tablet</small></p>
</section>

<section class="packet front green" style="left:312px; top:113px;">
  <div class="band">Clinically Approved</div>
  <div class="badge" role="img" aria-label="Round emblem of tablets"></div>
  <p class="supplement">Dietary Supplement</p>
  <h2 class="name">gastrelle</h2>
  <p class="claims">Nausea Prevention<br>for Alcohol Use<br><span class="benefit">Protects Stomach<br>Neutralizes Acid</span></p>
  <div class="stomach" role="img" aria-label="Stomach illustration"></div>
  <svg class="swoosh" viewBox="0 0 280 80" preserveAspectRatio="none"><path d="M0 30 C90 70 190 10 280 20 L280 80 L0 80 Z" fill="var(--accent)"/></svg>
  <p class="dose">2 tablets · 1000 mg<small>Calcium Carbonate per tablet</small></p>
</section>

<section class="packet front orange" style="left:552px; top:113px;">
  <div class="band">Clinically Approved</div>
  <div class="badge" role="img" aria-label="Round emblem of tablets"></div>
  <p class="supplement">Dietary Supplement</p>
  <h2 class="name">gastrelle</h2>
  <p class="claims">Nausea Prevention<br>for Alcohol Use<br><span class="benefit">Protects Stomach<br>Neutralizes Acid</span></p>
  <div class="stomach" role="img" aria-label="Stomach illustration"></div>
  <svg class="swoosh" viewBox="0 0 280 80" preserveAspectRatio="none"><path d="M0 30 C90 70 190 10 280 20 L280 80 L0 80 Z" fill="var(--accent)"/></svg>
  <p class="dose">2 tablets · 1000 mg<small>Calcium Carbonate per tablet</small></p>
</section>

<!-- bottom row: backs -->
<section class="packet back red" style="left:72px; top:377px;">
  <svg class="icon-cut" viewBox="0 0 22 14"><circle cx="4" cy="4" r="3" fill="none" stroke="var(--ink)"/><circle cx="4" cy="10" r="3" fill="none" stroke="var(--ink)"/><path d="M6 5 L21 11 M6 9 L21 3" stroke="var(--ink)"/></svg>
  <h2 class="name">gastrelle</h2>
  <div class="facts">
    <h3>Ingredients</h3><p>Serving size 2 tablets. Calcium carbonate 1000 mg per tablet.</p>
    <h3>Directions</h3><p>Take two tablets before drinking. Chew well.</p>
    <h3>Warnings</h3><p>Keep out of reach of children.</p>
  </div>
  <div class="stomach" role="img" aria-label="Stomach illustration"></div>
  <svg class="swoosh" viewBox="0 0 280 80" preserveAspectRatio="none"><path d="M0 20 C90 60 190 0 280 15 L280 80 L0 80 Z" fill="var(--accent)"/></svg>
  <p class="site">gastrelle.example</p>
</section>

<section class="packet back green" style="left:312px; top:377px;">
  <svg class="icon-cut" viewBox="0 0 22 14"><circle cx="4" cy="4" r="3" fill="none" stroke="var(--ink)"/><circle cx="4" cy="10" r="3" fill="none" stroke="var(--ink)"/><path d="M6 5 L21 11 M6 9 L21 3" stroke="var(--ink)"/></svg>
  <h2 class="name">gastrelle</h2>
  <div class="facts">
    <h3>Ingredients</h3><p>Serving size 2 tablets. Calcium carbonate 1000 mg per tablet.</p>
    <h3>Directions</h3><p>Take two tablets before drinking. Chew well.</p>
    <h3>Warnings</h3><p>Keep out of reach of children.</p>
  </div>
  <div class="stomach" role="img" aria-label="Stomach illustration"></div>
  <svg class="swoosh" viewBox="0 0 280 80" preserveAspectRatio="none"><path d="M0 20 C90 60 190 0 280 15 L280 80 L0 80 Z" fill="var(--accent)"/></svg>
  <p class="site">gastrelle.example</p>
</section>

<section class="packet back orange" style="left:552px; top:377px;">
  <svg class="icon-cut" viewBox="0 0 22 14"><circle cx="4" cy="4" r="3" fill="none" stroke="var(--ink)"/><circle cx="4" cy="10" r="3" fill="none" stroke="var(--ink)"/><path d="M6 5 L21 11 M6 9 L21 3" stroke="var(--ink)"/></svg>
  <h2 class="name">gastrelle</h2>
  <div class="facts">
    <h3>Ingredients</h3><p>Serving size 2 tablets. Calcium carbonate 1000 mg per tablet.</p>
    <h3>Directions</h3><p>Take two tablets before drinking. Chew well.</p>
    <h3>Warnings</h3><p>Keep out of reach of children.</p>
  </div>
  <div class="stomach" role="img" aria-label="Stomach illustration"></div>
  <svg class="swoosh" viewBox="0 0 280 80" preserveAspectRatio="none"><path d="M0 20 C90 60 190 0 280 15 L280 80 L0 80 Z" fill="var(--accent)"/></svg>
  <p class="site">gastrelle.example</p>
</section>

<!-- series header -->
<h1 class="series-name">gastrelle</h1>
<p class="series-note">Full colour print option<br>Series - different colors +<br>gray (metallic foil)</p>

<!-- hanging card -->
<section class="hang-card">
  <div class="hang-hole"></div>
  <p class="card-supplement">Dietary Supplement</p>
  <p class="card-name">gastrelle</p>
  <div class="packet front red">
    <div class="band">Clinically Approved</div>
    <div class="badge" role="img" aria-label="Round emblem of tablets"></div>
    <p class="supplement">Dietary Supplement</p>
    <h2 class="name">gastrelle</h2>
    <p class="claims">Nausea Prevention<br>for Alcohol Use<br><span class="benefit">Protects Stomach<br>Neutralizes Acid</span></p>
    <div class="stomach" role="img" aria-label="Stomach illustration"></div>
    <svg class="swoosh" viewBox="0 0 280 80" preserveAspectRatio="none"><path d="M0 30 C90 70 190 10 280 20 L280 80 L0 80 Z" fill="var(--accent)"/></svg>
    <p class="dose">2 tablets · 1000 mg<small>Calcium Carbonate per tablet</small></p>
  </div>
</section>

</body>
</html>
```